Full Stationary
Business Cards & Stationery for Limo Service - Transportation
Business Cards & Stationery for Limo Service
Professional
Glen Harbury / Dale Pronto
President / General Manager
1187 Fenwick Blvd, Suite 300 Des Moines, IA 50317
844.RQT.CARZ
info@vantregocars.example
www.vantregocars.example
I don't want this card to be too cluttered but I want it to look super sharp and modern. I like modern font however I want it to remain similar to the logo and professional as we are handing these cards to operators throughout the United States.
Be creative. I am unsure of the future demand for QR codes. I have attached 3, one for the website, Facebook, and Twitter. Feel free to use them if you wish, however, if there is something new I am unaware of please feel free to use this new technology. As stated earlier, I am unsure how well these work in todays world versus a few years ago. I have used them previously on the backs of business cards and think it looks cool, however if I am mistaken of something different please let me know.

```html
<!DOCTYPE html>
<html lang="en">
<head>
<meta charset="utf-8">
<title>Vantrego Cars — Stationery Set</title>
<link rel="stylesheet" href="https://fonts.googleapis.com/css2?family=Montserrat:wght@400;500;600&display=swap">
<style>
  :root {
    --backdrop: #d8d1c7;
    --paper: #ffffff;
    --ink: #3f4043;
    --ink-soft: #8a8c90;
    --rule: #c9cacd;
    --cell: #f1f1f2;
    --band-dark: #505257;
    --band-mid: #8e9096;
    --band-light: #c7c8cc;
  }
  * { box-sizing: border-box; margin: 0; padding: 0; }
  html, body { width: 1200px; height: 372px; overflow: hidden; }
  body {
    background: var(--backdrop);
    font-family: "Montserrat", Arial, sans-serif;
    color: var(--ink);
    position: relative;
  }
  .sheet {
    position: absolute;
    background: var(--paper);
    box-shadow: 0 2px 6px rgba(0,0,0,.18);
    overflow: hidden;
  }
  .wordmark {
    display: flex; align-items: center; gap: 5px;
    font-weight: 600; color: var(--ink);
    letter-spacing: .12em; text-transform: uppercase; white-space: nowrap;
  }
  .wordmark .mark { background: var(--ink); flex: none; }

  /* business card */
  .business-card { left: 24px; top: 168px; width: 228px; height: 132px; }
  .business-card .wordmark { position: absolute; left: 14px; top: 12px; font-size: 10px; }
  .business-card .wordmark .mark { width: 10px; height: 10px; }
  .card-band {
    position: absolute; left: 0; right: 0; top: 46px; height: 40px;
    background: linear-gradient(90deg, var(--band-dark), var(--band-mid) 60%, var(--band-light));
    padding: 8px 14px; color: #fff;
  }
  .card-name { font-size: 10px; font-weight: 600; letter-spacing: .1em; text-transform: uppercase; }
  .card-title { font-size: 6.5px; letter-spacing: .08em; margin-top: 3px; }
  .card-contact { position: absolute; left: 14px; right: 10px; bottom: 9px; font-size: 5.5px; line-height: 1.55; color: var(--ink-soft); white-space: nowrap; }
  .card-contact svg { width: 5px; height: 5px; vertical-align: -0.5px; margin-right: 3px; }

  /* letterhead & fax */
  .letterhead, .fax-sheet { top: 24px; width: 200px; height: 336px; }
  .letterhead { left: 269px; }
  .fax-sheet { left: 494px; }
  .sheet-head { position: absolute; top: 16px; left: 0; right: 0; display: flex; justify-content: center; }
  .sheet-head .wordmark { font-size: 8px; }
  .sheet-head .wordmark .mark { width: 9px; height: 9px; }
  .sheet-foot {
    position: absolute; bottom: 14px; left: 14px; right: 14px;
    border-top: 1px solid var(--rule); padding-top: 4px;
    font-size: 4px; color: var(--ink-soft); text-align: center;
    white-space: nowrap;
  }
  .fax-title { position: absolute; top: 66px; right: 18px; font-size: 13px; font-weight: 500; color: var(--ink); }
  .fax-table {
    position: absolute; top: 86px; left: 14px; width: 172px;
    border-collapse: collapse; font-size: 4.5px; color: var(--ink-soft);
  }
  .fax-table td { border: 1px solid var(--rule); height: 11px; padding: 0 3px; }
  .fax-table td.label { width: 24px; background: var(--cell); }
  .fax-options {
    position: absolute; top: 140px; left: 14px; width: 172px;
    display: flex; justify-content: space-between;
    font-size: 3.8px; color: var(--ink-soft); white-space: nowrap;
  }
  .fax-options span { display: flex; align-items: center; }
  .fax-options span::before {
    content: ""; display: inline-block; width: 3.5px; height: 3.5px;
    border: .6px solid var(--ink-soft); margin-right: 1.5px; flex: none;
  }

  /* envelopes */
  .envelope-back { left: 768px; top: 84px; width: 184px; height: 130px; }
  .envelope-back svg.flap { position: absolute; inset: 0; }
  .envelope-back .wordmark { position: absolute; left: 50%; top: 30px; transform: translateX(-50%); font-size: 7.5px; }
  .envelope-back .wordmark .mark { width: 9px; height: 9px; }
  .envelope-band { left: 768px; top: 226px; width: 184px; height: 32px; }
  .envelope-band .band {
    position: absolute; left: 0; right: 0; top: 8px; height: 16px;
    background: linear-gradient(90deg, var(--band-light), var(--band-dark) 35%, var(--band-dark) 65%, var(--band-light));
    color: #fff; font-size: 5.5px; letter-spacing: .2em; text-align: center; line-height: 16px;
  }
  .envelope-front { left: 768px; top: 272px; width: 184px; height: 92px; }
  .envelope-front .wordmark { position: absolute; left: 12px; top: 12px; font-size: 7px; }
  .envelope-front .wordmark .mark { width: 8px; height: 8px; }
  .envelope-front .return { position: absolute; left: 12px; top: 26px; font-size: 4.3px; color: var(--ink-soft); line-height: 1.5; }
</style>
</head>
<body>

  <section class="sheet business-card" aria-label="Business card">
    <div class="wordmark"><span class="mark"></span>Vantrego Cars</div>
    <div class="card-band">
      <p class="card-name">Glen Harbury</p>
      <p class="card-title">President</p>
    </div>
    <div class="card-contact">
      <p><svg viewBox="0 0 10 10"><path d="M2 1l2 2-1 1.5c.8 1.5 1.5 2.2 3 3L7.5 6l2 2-1.5 1.5C4.5 9 1 5.5.5 2z" fill="#8a8c90"/></svg>844.RQT.CARZ</p>
      <p><svg viewBox="0 0 10 10"><rect x="0.5" y="2" width="9" height="6" fill="none" stroke="#8a8c90"/><path d="M.5 2l4.5 3.5L9.5 2" fill="none" stroke="#8a8c90"/></svg>info@vantregocars.example</p>
      <p><svg viewBox="0 0 10 10"><path d="M5 .5a3 3 0 0 1 3 3c0 2.5-3 6-3 6s-3-3.5-3-6a3 3 0 0 1 3-3z" fill="#8a8c90"/></svg>1187 Fenwick Blvd, Suite 300 Des Moines, IA 50317</p>
    </div>
  </section>

  <section class="sheet letterhead" aria-label="Letterhead">
    <div class="sheet-head"><div class="wordmark"><span class="mark"></span>Vantrego Cars</div></div>
    <p class="sheet-foot">1187 Fenwick Blvd, Suite 300 Des Moines, IA 50317 &nbsp;|&nbsp; 844.RQT.CARZ</p>
  </section>

  <section class="sheet fax-sheet" aria-label="Fax cover sheet">
    <div class="sheet-head"><div class="wordmark"><span class="mark"></span>Vantrego Cars</div></div>
    <p class="fax-title">Fax</p>
    <table class="fax-table">
      <tr><td class="label">To</td><td></td><td class="label">From</td><td></td></tr>
      <tr><td class="label">Fax</td><td></td><td class="label">Phone</td><td></td></tr>
      <tr><td class="label">Re</td><td></td><td class="label">Date</td><td></td></tr>
      <tr><td class="label">Pages</td><td></td><td class="label">CC</td><td></td></tr>
    </table>
    <div class="fax-options">
      <span>Urgent</span><span>For Review</span><span>Please Comment</span><span>Please Reply</span><span>Please Recycle</span>
    </div>
    <p class="sheet-foot">1187 Fenwick Blvd, Suite 300 Des Moines, IA 50317 &nbsp;|&nbsp; 844.RQT.CARZ</p>
  </section>

  <section class="sheet envelope-back" aria-label="Envelope, back">
    <svg class="flap" viewBox="0 0 184 130" preserveAspectRatio="none">
      <path d="M0 0 L92 62 L184 0" fill="none" stroke="#e2e2e2" stroke-width="1"/>
      <path d="M0 130 L70 70 M184 130 L114 70" fill="none" stroke="#eeeeee" stroke-width="1"/>
    </svg>
    <div class="wordmark"><span class="mark"></span>Vantrego Cars</div>
  </section>

  <section class="sheet envelope-band" aria-label="Envelope, sealed flap">
    <div class="band">www.vantregocars.example</div>
  </section>

  <section class="sheet envelope-front" aria-label="Envelope, front">
    <div class="wordmark"><span class="mark"></span>Vantrego Cars</div>
    <div class="return">
      <p>1187 Fenwick Blvd, Suite 300</p>
      <p>Des Moines, IA 50317</p>
    </div>
  </section>

</body>
</html>
```